Hispanic Financial Counseling and Advocate Firm seeks business card design

Looking for a clean, professional business card design. This is a firm that specializes in providing financial education, coaching, and planning to the Hispanic community. The name of the company is Valemar, which means to prosper. We need a design that is clean, professional, and invokes trust, professionalism, but also welcoming. Our logo is a plant growing from a hand to give the messaging of of being in control of growing your financial future and security. Its part of a larger organization names Celesta Financial Group, who's logo is a tree with multi colored branches. We have the back of the card designed so we just need the front designed. the back is blue, so front needs to be a different background color, not blue.

Target Market(s)

Hispanic Community looking to better their future

Industry/Entity Type

financial services

Contact Information for Business Card

contact info: Anselmo Ibarra Jr, 951-555-0147, info@celestafinancialgroup.example. Celestafinancialgroup.example. tag line: Para un mañana mas firme!

Requirements
Must have
• basics: logo, contact info.
Nice to have
• possibly incorporate the tree logo provided somehow
Should not have
• should not look like the back, needs to be different from the back provided.

```html
<!DOCTYPE html>
<html lang="es">
<head>
<meta charset="utf-8">
<title>Valemar – Tarjetas de presentación</title>
<link rel="stylesheet" href="https://fonts.googleapis.com/css2?family=Montserrat:wght@300;400;600;700;800&family=Open+Sans:wght@400;600&display=swap">
<style>
  :root {
    --stage: #8a8a8a;
    --paper: #ffffff;
    --slate: #4a5773;
    --leaf: #6aaa35;
    --leaf-soft: #a9d37f;
    --navy: #0e3047;
    --navy-ink: #3e4a66;
    --white: #ffffff;
    --drop-green: #7cc242;
    --drop-blue: #2fa6de;
    --drop-red: #e8413c;
    --drop-purple: #9b6fc0;
    --drop-orange: #f2b51c;
  }
  * { box-sizing: border-box; margin: 0; padding: 0; }
  html, body { width: 1200px; height: 900px; overflow: hidden; }
  body { background: var(--stage); font-family: "Open Sans", sans-serif; position: relative; }

  .card {
    position: absolute;
    width: 560px;
    height: 320px;
    border-radius: 6px;
    overflow: hidden;
    box-shadow: 0 10px 24px rgba(0,0,0,0.28);
  }

  /* ---------- Front ---------- */
  .card-front { left: 50px; top: 110px; background: var(--paper); }
  .front-waves { position: absolute; inset: 0; }
  .front-illustration {
    position: absolute; left: 40px; top: 18px; width: 170px; height: 125px;
    border-radius: 50% 50% 40% 40%;
    background: radial-gradient(ellipse at 55% 40%, var(--leaf-soft) 0%, var(--leaf) 70%);
    opacity: 0.85;
  }
  .front-brand {
    position: absolute; left: 300px; top: 58px;
    display: flex; align-items: center; gap: 12px;
  }
  .brand-dot { width: 34px; height: 34px; border-radius: 50%; background: var(--leaf); flex: none; }
  .brand-text { border-left: 1px solid #b9bfcc; padding-left: 12px; }
  .brand-name {
    font-family: "Montserrat", sans-serif; font-weight: 600;
    font-size: 40px; line-height: 1; color: var(--leaf); letter-spacing: -0.5px;
  }
  .brand-sub {
    font-family: "Montserrat", sans-serif; font-weight: 700;
    font-size: 10.5px; letter-spacing: 1.6px; color: var(--navy-ink); margin-top: 4px;
  }
  .person-name {
    position: absolute; left: 250px; top: 140px;
    font-family: "Montserrat", sans-serif; font-weight: 700; font-size: 19px; letter-spacing: 1px;
  }
  .person-name .given { color: var(--leaf); }
  .person-name .family { color: var(--navy-ink); }
  .contact-list {
    position: absolute; right: 26px; top: 178px; list-style: none;
    text-align: right; font-size: 14px; color: #222;
  }
  .contact-list li { display: flex; align-items: center; justify-content: flex-end; gap: 8px; margin-bottom: 6px; }
  .contact-icon { width: 18px; height: 18px; flex: none; }
  .front-web {
    position: absolute; right: 34px; bottom: 18px;
    color: var(--white); font-size: 16px; font-weight: 400;
  }

  /* ---------- Back ---------- */
  .card-back { left: 590px; top: 470px; background: var(--navy); color: var(--white); }
  .back-brand {
    position: absolute; left: 40px; top: 42px;
    display: flex; align-items: center; gap: 16px;
  }
  .back-brand .brand-dot { width: 56px; height: 56px; background: var(--white); }
  .back-brand .brand-text { border-left: 1px solid rgba(255,255,255,0.6); padding-left: 16px; }
  .back-name {
    font-family: "Montserrat", sans-serif; font-weight: 800; font-size: 58px; line-height: 1;
    letter-spacing: -1px; color: var(--white);
  }
  .back-sub {
    font-family: "Montserrat", sans-serif; font-weight: 300; font-size: 22px; color: var(--white);
  }
  .services {
    position: absolute; left: 40px; top: 170px; width: 480px;
    display: flex; flex-wrap: wrap; gap: 4px 16px; list-style: none;
    font-family: "Montserrat", sans-serif; font-size: 14px;
  }
  .services li { display: flex; align-items: center; gap: 5px; }
  .drop { width: 7px; height: 10px; border-radius: 50% 50% 50% 50% / 60% 60% 40% 40%; }
  .tagline {
    position: absolute; left: 40px; right: 40px; bottom: 40px;
    display: flex; align-items: center; gap: 12px;
    font-family: "Montserrat", sans-serif; font-weight: 600; font-size: 14px; letter-spacing: 1.5px;
    white-space: nowrap;
  }
  .tagline .rule { flex: 1; height: 2px; background: var(--white); }
</style>
</head>
<body>

<section class="card card-front" aria-label="Frente de la tarjeta">
  <svg class="front-waves" viewBox="0 0 560 320" aria-hidden="true">
    <path d="M0 120 C60 170 110 235 250 252 C380 266 470 262 560 280 L560 320 L0 320 Z" fill="var(--slate)"/>
    <path d="M0 118 C70 180 130 238 260 250 C380 260 470 258 560 276" fill="none" stroke="var(--white)" stroke-width="7"/>
    <path d="M40 150 C110 212 170 236 280 244 C400 252 480 252 560 268" fill="none" stroke="var(--leaf)" stroke-width="3"/>
  </svg>

  <div class="front-illustration" role="img" aria-label="Ilustración de una planta con hojas verdes que crece desde una mano"></div>

  <div class="front-brand">
    <span class="brand-dot"></span>
    <div class="brand-text">
      <div class="brand-name">Valemar</div>
      <div class="brand-sub">SERVICIOS FINANCIEROS</div>
    </div>
  </div>

  <p class="person-name"><span class="given">ANSELMO</span> <span class="family">IBARRA JR</span></p>

  <ul class="contact-list">
    <li>951-555-0147
      <svg class="contact-icon" viewBox="0 0 18 18" aria-hidden="true"><circle cx="9" cy="9" r="9" fill="var(--navy-ink)"/><path d="M6 4.5 L7.6 4.5 L8.3 7 L7.2 7.8 C7.7 9 8.7 10.2 10 10.8 L10.9 9.8 L13.4 10.5 L13.4 12 C12 13.4 9 12.8 7 10.8 C5 8.8 4.6 6 6 4.5 Z" fill="#fff"/></svg>
    </li>
    <li>info@celestafinancialgroup.example
      <svg class="contact-icon" viewBox="0 0 18 18" aria-hidden="true"><circle cx="9" cy="9" r="9" fill="var(--navy-ink)"/><rect x="4.5" y="6" width="9" height="6.4" fill="none" stroke="#fff" stroke-width="1.2"/><path d="M4.5 6 L9 9.6 L13.5 6" fill="none" stroke="#fff" stroke-width="1.2"/></svg>
    </li>
  </ul>

  <p class="front-web">Celestafinancialgroup.example</p>
</section>

<section class="card card-back" aria-label="Reverso de la tarjeta">
  <div class="back-brand">
    <span class="brand-dot"></span>
    <div class="brand-text">
      <div class="back-name">Celesta</div>
      <div class="back-sub">Financial Group Inc</div>
    </div>
  </div>

  <ul class="services">
    <li><span class="drop" style="background:var(--drop-green)"></span>Inmigración</li>
    <li><span class="drop" style="background:var(--drop-blue)"></span>Planificacion Financiera</li>
    <li><span class="drop" style="background:var(--drop-red)"></span>Seguros</li>
    <li><span class="drop" style="background:var(--drop-purple)"></span>Impuestos</li>
    <li><span class="drop" style="background:var(--drop-red)"></span>Y mas</li>
    <li><span class="drop" style="background:var(--drop-orange)"></span>Preparación de documentos</li>
  </ul>

  <p class="tagline"><span class="rule"></span>PARA UN MAÑANA MAS FIRME!<span class="rule"></span></p>
</section>

</body>
</html>
```